Corporate Design für Abwicklung von Lohn- und Gehaltsabrechnungen
Super flexible Zusammenarbeit, alle Änderungen wurden zeitnah zur Ansicht geliefert. Sehr kreatives und einheitliches Ergebnis für das neue CI. Immer wieder gerne!!!
Zielgruppe
Wir wickeln die Lohn- und Gehaltsabrechnung für kleine bis mittlere Unternehmen ab.
Aufgabenstellung
Das bereits bestehende Logo kann gerne noch einmal, aber ähnlich von den Abmessungen und Farben her, geändert werden.
Insgesamt modernes und junges Auftreten.
Wichtig ist das Grün #3dae62
RGB 61 174 98
Wir wünschen uns ein einheitliches Corporate Design bestehend aus Briefpapier, Visitenkarten, Briefumschlägen und Schreibblöcken, angelehnt an das bereits vorhandene Logo.
Briefpapier, gerne 2-seitig mit grüner Rückseite
Endformat 210x297mm hoch
Visitenkarten 2-seitig, 85x55mm quer oder hoch (lassen uns gerne überraschen)
Die beigefügte Visitenkarte ist leider mit alten Daten, hat uns vom Prinzip her aber gut gefallen. Die neue sollte sich aber im Corporate Design Wiederspiegeln mit folgenden Daten:
Briefumschläge C4 (229 x 324mm Endformat) Hoch
Schreibblöcke A5 148x210 Endformat hoch
Schriftart Poppins

```html
<!DOCTYPE html>
<html lang="de">
<head>
<meta charset="utf-8">
<title>lohnwerk – Corporate Design</title>
<link href="https://fonts.googleapis.com/css2?family=Poppins:wght@500;600&family=Lato:wght@400;700&display=swap" rel="stylesheet">
<style>
  :root {
    --green: #3dae62;
    --green-light: #8fcf9e;
    --mint: #e7f3e6;
    --ink: #3a3a3a;
    --ground: #ebe8e3;
    --paper: #ffffff;
  }
  * { margin: 0; padding: 0; box-sizing: border-box; }
  html, body { width: 1200px; height: 1200px; overflow: hidden; }
  body { background: var(--ground); font-family: "Lato", sans-serif; color: var(--ink); position: relative; }

  .sheet { position: absolute; box-shadow: 0 3px 10px rgba(0,0,0,.18); }
  .brand { font-family: "Poppins", sans-serif; font-weight: 600; letter-spacing: -.01em; white-space: nowrap; line-height: 1; }

  /* Letter back side */
  .letter-back { left: 282px; top: 230px; width: 472px; height: 667px; background: var(--green); }
  .letter-back .brand-top { position: absolute; left: 42px; top: 22px; font-size: 28px; color: var(--green-light); }
  .letter-back .brand-foot { position: absolute; right: 16px; bottom: 34px; font-size: 17px; color: var(--green-light); }

  /* Follow-up page */
  .letter-follow { left: 98px; top: 300px; width: 430px; height: 608px; background: var(--mint); }
  .letter-follow .brand { position: absolute; left: 28px; top: 58px; font-size: 15px; color: var(--green); }

  /* Letter front */
  .letter { left: 217px; top: 343px; width: 432px; height: 611px; background: var(--paper); }
  .letter::after { content: ""; position: absolute; left: 0; right: 0; bottom: 0; height: 8px; background: var(--mint); }
  .letter .brand-mark { position: absolute; left: 42px; top: 44px; font-size: 24px; color: var(--green); }
  .letter .brand-word { position: absolute; right: 37px; top: 40px; font-size: 17px; color: var(--green); }
  .sender-line { position: absolute; left: 48px; top: 103px; font-size: 4.6px; color: #555; }
  .contact { position: absolute; right: 37px; top: 66px; text-align: right; font-size: 5.6px; line-height: 1.4; }
  .contact .gap { height: 8px; }
  .fold { position: absolute; left: 0; width: 6px; border-top: 0.7px solid #999; }
  .letter-body { position: absolute; left: 42px; top: 227px; width: 275px; font-size: 6.4px; line-height: 1.38; }
  .letter-body p { margin-bottom: 8px; }
  .closing { position: absolute; left: 42px; top: 415px; font-size: 6.4px; }
  .signature { position: absolute; left: 50px; top: 422px; width: 46px; height: 26px; background: rgba(30,70,150,.18); border-radius: 4px; }
  .signer { position: absolute; left: 42px; top: 446px; font-size: 6.4px; }
  .bank { position: absolute; right: 37px; bottom: 25px; text-align: right; font-size: 5.6px; line-height: 1.35; }

  /* Business cards */
  .card-front { left: 781px; top: 260px; width: 174px; height: 113px; background: var(--green); display: flex; align-items: center; justify-content: center; }
  .card-front .brand { font-size: 19px; color: #fff; }
  .card-back { left: 781px; top: 391px; width: 174px; height: 113px; background: var(--mint); }
  .card-back .brand { position: absolute; left: 16px; top: 14px; font-size: 12px; color: var(--green); }
  .card-back .person { position: absolute; left: 16px; top: 48px; font-size: 6.5px; color: var(--green); font-weight: 700; line-height: 1.3; }
  .card-back .person span { display: block; font-weight: 400; font-size: 4.6px; color: var(--ink); }
  .card-back .details { position: absolute; left: 98px; top: 48px; font-size: 4.6px; line-height: 1.4; }
  .card-back .details .gap { height: 6px; }

  /* Notepad A5 */
  .notepad { left: 781px; top: 522px; width: 305px; height: 432px; background: var(--green); }
  .notepad .brand { position: absolute; left: 0; right: 0; top: 220px; text-align: center; font-size: 40px; color: #fff; }
  .notepad .tagline { position: absolute; left: 0; right: 0; top: 350px; text-align: center; font-size: 12px; line-height: 1.35; letter-spacing: .02em; color: #fff; }
  .notepad .mark { position: absolute; left: 146px; top: 400px; width: 13px; height: 13px; background: var(--green-light); }
</style>
</head>
<body>

  <section class="sheet letter-back" aria-label="Briefpapier Rückseite">
    <div class="brand brand-top">lohnwerk</div>
    <div class="brand brand-foot">lohnwerk</div>
  </section>

  <section class="sheet letter-follow" aria-label="Briefpapier Folgeseite">
    <div class="brand">lohnwerk</div>
  </section>

  <section class="sheet letter" aria-label="Briefpapier Vorderseite">
    <div class="brand brand-mark">lohnwerk</div>
    <div class="brand brand-word">lohnwerk</div>
    <div class="sender-line">lohnwerk &nbsp;|&nbsp; Jonas Berger &nbsp;|&nbsp; Lindenweg 12 &nbsp;|&nbsp; 10115 Musterstadt</div>
    <div class="contact">
      Jonas Berger<br>Lindenweg 12<br>10115 Musterstadt
      <div class="gap"></div>
      Tel. 030 554210 40<br>Fax 030 554210 49<br>Mail: post@lohnwerk-beispiel.de<br>Web: www.lohnwerk-beispiel.de
    </div>
    <div class="fold" style="top:216px"></div>
    <div class="fold" style="top:305px"></div>
    <div class="fold" style="top:433px"></div>
    <div class="letter-body">
      <p>Sehr geehrter Herr Max Muster,</p>
      <p>Sed ut perspiciatis unde omnis iste natus error sit voluptatem accusantium doloremque laudantium, totam rem aperiam, eaque ipsa quae ab illo inventore veritatis et quasi architecto beatae vitae dicta sunt explicabo.</p>
      <p>Nemo enim ipsam voluptatem quia voluptas sit aspernatur aut odit aut fugit, sed quia consequuntur magni dolores eos qui ratione voluptatem sequi nesciunt. Neque porro quisquam est, qui dolorem ipsum quia dolor sit amet, consectetur, adipisci velit, sed quia non numquam eius modi tempora incidunt ut labore et dolore magnam aliquam quaerat voluptatem.</p>
      <p>Ut enim ad minima veniam, quis nostrum exercitationem ullam corporis suscipit laboriosam, nisi ut aliquid ex ea commodi consequatur? Quis autem vel eum iure reprehenderit qui in ea voluptate velit esse quam nihil molestiae consequatur, vel illum qui dolorem eum fugiat quo voluptas nulla pariatur?</p>
    </div>
    <div class="closing">Mit freundlichen Grüßen</div>
    <div class="signature" role="img" aria-label="Handschriftliche Unterschrift"></div>
    <div class="signer">Paul Beispiel</div>
    <div class="bank">Bankverbindung:<br>IBAN DE 0000111122223333<br>BIC BEISPBANK</div>
  </section>

  <section class="sheet card-front" aria-label="Visitenkarte Vorderseite">
    <div class="brand">lohnwerk</div>
  </section>

  <section class="sheet card-back" aria-label="Visitenkarte Rückseite">
    <div class="brand">lohnwerk</div>
    <div class="person">Jonas Berger<span>Geschäftsführer</span></div>
    <div class="details">
      Lindenweg 12<br>10115 Musterstadt
      <div class="gap"></div>
      Tel. 030 554210 40<br>Fax 030 554210 49<br>Mail: post@lohnwerk-beispiel.de<br>Web: www.lohnwerk-beispiel.de
    </div>
  </section>

  <section class="sheet notepad" aria-label="Schreibblock A5">
    <div class="brand">lohnwerk</div>
    <div class="tagline">LOHNBUCHHALTUNG<br>EINFACH OUTSOURCEN</div>
    <div class="mark"></div>
  </section>

</body>
</html>
```